Kestrelwood Pathways Agency business cards

Australian company about to start offering its services. We recruit international students to come to study English, vocational education and postgraduate courses in Australia. We help them find the institution and select the right city they want to come to Australia. We are a young, online oriented and supportive agency. Our clients are between 18 and 35 years old, mainly University students, young professionals or people with work experience. We provide much more information that any other agency offer. We administrate a Facebook group with more than 11.000 members that daily ask questions about general information when coming to Australia, while they are here and even after they leave the country

Target Market(s)

International students from South America, Central America and Europe

Industry/Entity Type

Student

Contact Information for Business Card

Tomas Brevik
Managing Director
tomas@velmorin.com.au
www.velmorin.com.au
+61 491058263
Melbourne, Australia

Font styles to use
Serif
Sans Serif

Colors

Designer to choose colors to be used in the design.

Requirements
Must have
• Horizontal design
• Standard business card size and shape. If font uses green or yellow colours, they will have to match the ones from the logo
Nice to have
• UPDATE: Use the contents of the green image to design one of the card sides. Use our logo in the background of that side as watermark.
• Passport image, or immigration stamps. A picture of the Yarra River (from Melbourne) would be cool as well.
Should not have
• Non-standard business card size and shape
• Not black as the background colour of any sides as we are not a VIP agency or a hight class service. We are orientes to young people and they like colours, pictures, something attractive.
• Vertical design
• NO YELLOW or BLACK AS THE BACKGROUND COLOUR OF ANY SIDE OF THE BIZ CARD

```html
<!DOCTYPE html>
<html lang="en">
<head>
<meta charset="UTF-8">
<title>Kestrelwood Pathways Agency — Business Cards</title>
<link href="https://fonts.googleapis.com/css2?family=Ubuntu:wght@400;500;700&display=swap" rel="stylesheet">
<style>
  :root {
    --brand-green: #12623b;
    --brand-green-dark: #0d5232;
    --brand-yellow: #f0c419;
    --paper: #f4f4f2;
    --ink: #4a4a4a;
    --divider: #c9c9c9;
    --backdrop: #e6e3de;
  }
  * { margin: 0; padding: 0; box-sizing: border-box; }
  html, body {
    width: 1200px; height: 886px; overflow: hidden;
    background: var(--backdrop);
    font-family: "Ubuntu", sans-serif;
  }
  .sheet { position: relative; width: 1200px; height: 886px; }
  .card {
    position: absolute; left: 330px; width: 540px; height: 330px;
    border-radius: 22px; overflow: hidden;
    box-shadow: 0 10px 24px rgba(0,0,0,0.18);
  }
  .card--front { top: 83px; background: var(--brand-green); }
  .card--back { top: 473px; background: var(--paper); }

  .front-name {
    position: absolute; inset: 0;
    display: flex; align-items: center; justify-content: center; gap: 14px;
    color: var(--brand-yellow); font-weight: 700; font-size: 58px; letter-spacing: 1px;
  }
  .front-name .dot { width: 22px; height: 22px; border-radius: 50%; background: var(--brand-yellow); }

  .back-wave { position: absolute; inset: 0; }
  .back-name {
    position: absolute; left: 40px; top: 108px; width: 200px;
    display: flex; align-items: center; gap: 10px;
    color: var(--brand-green); font-weight: 700; font-size: 34px;
  }
  .back-name .dot { width: 14px; height: 14px; border-radius: 50%; background: var(--brand-yellow); }
  .divider {
    position: absolute; left: 262px; top: 40px; width: 1px; height: 150px;
    background: var(--divider);
  }
  .contact { position: absolute; left: 282px; top: 42px; }
  .contact .person { color: var(--brand-green); font-weight: 700; font-size: 21px; }
  .contact .role { color: var(--brand-yellow); font-weight: 500; font-size: 15px; margin-top: 2px; margin-bottom: 10px; }
  .contact ul { list-style: none; }
  .contact li {
    display: flex; align-items: center; gap: 8px;
    color: var(--ink); font-size: 13px; line-height: 20px;
  }
  .contact li svg { width: 12px; height: 12px; flex: none; fill: var(--brand-green); }
  .tagline {
    position: absolute; right: 28px; bottom: 118px;
    color: #fff; font-weight: 500; font-size: 15px;
    transform: rotate(-22deg); transform-origin: right bottom;
  }
</style>
</head>
<body>
<main class="sheet">
  <section class="card card--front" aria-label="Card front">
    <div class="front-name"><span class="dot"></span>Velmorin</div>
  </section>

  <section class="card card--back" aria-label="Card back">
    <svg class="back-wave" viewBox="0 0 540 330" preserveAspectRatio="none">
      <path d="M0,300 C170,300 360,270 540,112 L540,330 L0,330 Z" fill="var(--brand-green)"/>
      <path d="M0,290 C170,288 360,250 540,96" fill="none" stroke="var(--brand-yellow)" stroke-width="6"/>
    </svg>

    <div class="back-name"><span class="dot"></span>Velmorin</div>
    <div class="divider"></div>

    <div class="contact">
      <p class="person">Tomas Brevik</p>
      <p class="role">Managing Director</p>
      <ul>
        <li><svg viewBox="0 0 12 12"><path d="M2.5 0.5 L4.5 0.5 L5.3 3 L4 4.2 C4.6 5.6 6.4 7.4 7.8 8 L9 6.7 L11.5 7.5 L11.5 9.5 C11.5 10.6 10.6 11.5 9.5 11.5 C4.5 11.2 0.8 7.5 0.5 2.5 C0.5 1.4 1.4 0.5 2.5 0.5 Z"/></svg>+61 491058263</li>
        <li><svg viewBox="0 0 12 12"><path d="M0.5 2 H11.5 V10 H0.5 Z M1.2 2.6 L6 6.4 L10.8 2.6" stroke="#fff" stroke-width="0.8"/></svg>tomas@velmorin.com.au</li>
        <li><svg viewBox="0 0 12 12"><circle cx="6" cy="6" r="5.5"/><path d="M0.5 6 H11.5 M6 0.5 C3.5 3 3.5 9 6 11.5 M6 0.5 C8.5 3 8.5 9 6 11.5" stroke="#fff" stroke-width="0.8" fill="none"/></svg>www.velmorin.com.au</li>
        <li><svg viewBox="0 0 12 12"><path d="M6 0.5 C3.5 0.5 1.8 2.3 1.8 4.6 C1.8 7.6 6 11.5 6 11.5 C6 11.5 10.2 7.6 10.2 4.6 C10.2 2.3 8.5 0.5 6 0.5 Z"/><circle cx="6" cy="4.6" r="1.6" fill="#fff"/></svg>Melbourne, Australia</li>
      </ul>
    </div>

    <p class="tagline">Hacemos más por ti!</p>
  </section>
</main>
</body>
</html>
```